willowcreekrestoring - healing business promotion

I have and energy / intuitive healing and kinesiology business. working with people who are looking for healing outside of the modern medical model, who have tried but failed in their search for understanding their conditions and why health and or happiness eludes them. the healing is done with love, patience and understanding. I am looking to be taken seriously with my presentation and to reach a person who may be deterred by the thought of angels and intuition! but to not exclude those that are attracted to that also.

Industry/Entity Type

Medical

Contact Information for Business Card

willowcreekrestoring
fast safe deep energy healing system
tamsin louise harte
energy healing / kinesiology and neurotraining
0417266183 07 4158 2746
home visits available for cairns and tablelands
t.lharte@quillmail.com

Requirements
Should not have
• Primary colours

```html
<!DOCTYPE html>
<html lang="en">
<head>
<meta charset="utf-8">
<title>willow creek restoring – appointment card</title>
<link rel="stylesheet" href="https://fonts.googleapis.com/css2?family=Poiret+One&display=swap">
<style>
  :root {
    --violet: #9a2cf5;
    --violet-line: #a863f0;
    --paper: #ffffff;
    --gold: #f2e21a;
    --header-coral: #f48a5e;
    --header-peach: #f2b08c;
    --header-lilac: #eeb4ee;
    --footer-crimson: #c8325e;
    --footer-rose: #d24a86;
    --footer-orchid: #cf5ba4;
  }
  html, body {
    margin: 0;
    padding: 0;
    width: 1200px;
    height: 741px;
    overflow: hidden;
    background: var(--paper);
  }
  .card {
    position: relative;
    width: 1200px;
    height: 741px;
    background: var(--paper);
    font-family: "Poiret One", sans-serif;
    color: var(--violet);
    overflow: hidden;
  }
  .card__header {
    position: absolute;
    left: 0; top: 0;
    width: 1200px;
    height: 109px;
    background:
      radial-gradient(ellipse 420px 110px at 560px 10px, var(--header-lilac) 0%, rgba(238,180,238,0) 100%),
      linear-gradient(90deg, var(--header-coral) 0%, var(--header-peach) 30%, var(--header-lilac) 50%, var(--header-peach) 72%, var(--header-coral) 100%);
  }
  .brand-name {
    position: absolute;
    left: 36px;
    right: 24px;
    top: 6px;
    margin: 0;
    font-size: 72px;
    font-weight: 400;
    letter-spacing: 0.27em;
    white-space: nowrap;
    text-align: center;
    color: var(--violet);
    text-shadow: 0 0 6px #fff, 0 0 12px rgba(255,255,255,0.8);
  }
  .appointment__heading {
    position: absolute;
    left: 0; width: 1200px;
    top: 118px;
    margin: 0;
    text-align: center;
    font-size: 56px;
    font-weight: 400;
    letter-spacing: 0.17em;
  }
  .appointment__row {
    position: absolute;
    top: 196px;
    font-size: 54px;
    letter-spacing: 0.12em;
    white-space: nowrap;
  }
  .appointment__date { left: 76px; }
  .appointment__time { left: 660px; }
  .home-support {
    position: absolute;
    left: 76px;
    top: 332px;
    font-size: 54px;
    letter-spacing: 0.1em;
    white-space: nowrap;
  }
  .writing-lines {
    position: absolute;
    left: 0; top: 0;
  }
  .card__footer {
    position: absolute;
    left: 0; top: 627px;
    width: 1200px;
    height: 114px;
    background:
      radial-gradient(ellipse 300px 60px at 620px 0px, rgba(240,130,110,0.55) 0%, rgba(240,130,110,0) 100%),
      linear-gradient(90deg, var(--footer-crimson) 0%, var(--footer-rose) 45%, var(--footer-orchid) 100%);
  }
  .phone {
    position: absolute;
    top: 22px;
    margin: 0;
    font-size: 64px;
    letter-spacing: 0.04em;
    color: var(--gold);
    text-shadow: 0 0 3px rgba(120,40,20,0.6);
    white-space: nowrap;
  }
  .phone--mobile { left: 54px; }
  .phone--landline { left: 722px; }
</style>
</head>
<body>
<main class="card">
  <header class="card__header">
    <h1 class="brand-name">willow creek restoring</h1>
  </header>

  <h2 class="appointment__heading">your next appointment</h2>
  <div class="appointment__row appointment__date">date __ / __ / __</div>
  <div class="appointment__row appointment__time">time&nbsp; __:__am/pm</div>

  <div class="home-support">home support:</div>

  <svg class="writing-lines" width="1200" height="741" aria-hidden="true">
    <g stroke="var(--violet-line)" stroke-width="1.6">
      <line x1="487" y1="387" x2="1133" y2="387"/>
      <line x1="71" y1="449" x2="1137" y2="449"/>
      <line x1="71" y1="510" x2="1137" y2="510"/>
      <line x1="71" y1="570" x2="1137" y2="570"/>
    </g>
  </svg>

  <footer class="card__footer">
    <p class="phone phone--mobile">0417 266 183</p>
    <p class="phone phone--landline">07 4158 2746</p>
  </footer>
</main>
</body>
</html>
```